Permanent Makeup Certificate for Lash Craft Institute Certified Artists

I need a beautifully designed certificate for my students who have successfully obtained my certification for Eyebrow Micropigmentation.

I have attached my sample certificate in InDesign format. This certificate is how I want the Certified Artist Certificate to read. My wording is extremely important for US Insurance reasons. I would like it to be in 11 x 17 inch format for USA printing.

I have also attached samples of certificates from other companies to give you an idea of how fancy I would like it to be. My company colors are pink and white, so I would like the dominant colors to be shades of pink and white. I like pink pastel combines with darker shades of pink and white. If the design calls for another color in addition to pink, that would also be great. I really like the colors in the Venmara Certificate.

I have attached a copy of my signature in .png

Target Market(s)

Beauty Industry

Industry/Entity Type

Artists

Font styles to use
Serif
Script

Colors
ffffff
f9d9e8
9bcb3c
cadf82
e667a6
e34297
eea4c8
b7a5cd

Requirements
Must have
• Wording exactly as I uploaded in InDesign file
Nice to have
• Beautiful images of female face, I am not sure if I like this idea. Just an experiement

```html
<!DOCTYPE html>
<html lang="en">
<head>
<meta charset="utf-8">
<title>Certificate of Excellence – Lash Craft Institute</title>
<link rel="stylesheet" href="https://fonts.googleapis.com/css2?family=Pinyon+Script&family=Open+Sans:wght@400;600;700&family=Playfair+Display:wght@500&display=swap">
<style>
  :root {
    --canvas: #f4f4f4;
    --magenta: #e6007e;
    --rose: #e34297;
    --blush: #f9d9e8;
    --petal: #eea4c8;
    --ink: #444444;
    --ink-soft: #666666;
    --white: #ffffff;
  }
  html, body {
    margin: 0;
    padding: 0;
    width: 1200px;
    height: 978px;
    overflow: hidden;
    background: var(--canvas);
  }
  .certificate {
    position: absolute;
    left: 40px;
    top: 126px;
    width: 1120px;
    height: 726px;
    box-sizing: border-box;
    border: 17px solid var(--magenta);
    background: var(--white);
    box-shadow: 0 4px 14px rgba(0,0,0,0.25);
    font-family: "Open Sans", sans-serif;
    color: var(--ink);
  }
  .portrait-area {
    position: absolute;
    left: 560px;
    top: 0;
    right: 0;
    bottom: 0;
    background:
      radial-gradient(ellipse at 75% 45%, #f3c9ba 0%, rgba(243,201,186,0) 45%),
      radial-gradient(ellipse at 40% 85%, var(--petal) 0%, rgba(238,164,200,0) 50%),
      linear-gradient(90deg, rgba(249,217,232,0) 0%, var(--blush) 30%, #f5bcd6 100%);
  }
  .frame-line {
    position: absolute;
    inset: 16px;
    border: 2px solid var(--petal);
    pointer-events: none;
  }
  .frame-line.inner {
    inset: 22px;
    border: 1px solid var(--blush);
  }
  .brand {
    position: absolute;
    left: 150px;
    top: 150px;
    width: 456px;
    text-align: center;
    display: flex;
    justify-content: center;
    align-items: center;
    gap: 10px;
  }
  .brand-dot {
    width: 14px;
    height: 14px;
    border-radius: 50%;
    background: var(--rose);
  }
  .brand-name {
    font-family: "Playfair Display", serif;
    font-weight: 500;
    font-size: 34px;
    color: #8a2a6e;
  }
  .title {
    position: absolute;
    left: 100px;
    top: 248px;
    width: 556px;
    text-align: center;
    font-family: "Pinyon Script", cursive;
    font-size: 46px;
    color: var(--ink);
    margin: 0;
    font-weight: normal;
  }
  .lead {
    position: absolute;
    left: 100px;
    top: 321px;
    width: 556px;
    text-align: center;
    font-size: 14px;
    letter-spacing: 0.3px;
    color: var(--ink-soft);
  }
  .recipient {
    position: absolute;
    left: 100px;
    top: 380px;
    width: 556px;
    text-align: center;
    font-family: "Pinyon Script", cursive;
    font-size: 36px;
    color: var(--ink);
  }
  .recipient-rule {
    position: absolute;
    left: 125px;
    top: 420px;
  }
  .statement {
    position: absolute;
    left: 100px;
    top: 464px;
    width: 556px;
    text-align: center;
    font-size: 14px;
    line-height: 18px;
    color: var(--ink-soft);
  }
  .statement strong { color: var(--ink); font-weight: 700; }
  .date-block {
    position: absolute;
    left: 170px;
    top: 572px;
    width: 120px;
    text-align: center;
  }
  .date-value {
    font-size: 14px;
    color: var(--ink-soft);
    padding-bottom: 4px;
    border-bottom: 1px solid #999;
  }
  .caption {
    font-size: 9px;
    color: var(--ink-soft);
    margin-top: 6px;
  }
  .signature-block {
    position: absolute;
    left: 440px;
    top: 560px;
    width: 190px;
    text-align: center;
  }
  .signature-mark {
    height: 30px;
    margin: 0 10px;
    background: linear-gradient(90deg, rgba(68,68,68,0) 0%, rgba(68,68,68,0.12) 50%, rgba(68,68,68,0) 100%);
    border-bottom: 1px solid #999;
  }
  .signer {
    font-size: 9px;
    line-height: 12px;
    color: var(--ink-soft);
    margin-top: 6px;
  }
  .signer strong { color: var(--ink); font-weight: 600; }
</style>
</head>
<body>
  <main class="certificate">
    <div class="portrait-area" role="img" aria-label="Soft-focus beauty portrait of a woman with pink orchids"></div>
    <div class="frame-line"></div>
    <div class="frame-line inner"></div>

    <div class="brand">
      <span class="brand-dot"></span>
      <span class="brand-name">Lash Craft Institute</span>
    </div>

    <h1 class="title">Certificate of Excellence</h1>
    <div class="lead">THIS IS TO CERTIFY THAT</div>

    <div class="recipient">John Noname Doe</div>
    <svg class="recipient-rule" width="480" height="26" viewBox="0 0 480 26" aria-hidden="true">
      <line x1="20" y1="13" x2="460" y2="13" stroke="#777" stroke-width="1.2"/>
      <path d="M20 13 C10 13 6 6 12 4 M20 13 C10 13 6 20 12 22" fill="none" stroke="#777" stroke-width="1.2"/>
      <path d="M460 13 C470 13 474 6 468 4 M460 13 C470 13 474 20 468 22" fill="none" stroke="#777" stroke-width="1.2"/>
      <rect x="228" y="9" width="24" height="8" fill="#fff"/>
      <circle cx="233" cy="13" r="1.2" fill="#777"/>
      <circle cx="240" cy="13" r="1.2" fill="#777"/>
      <circle cx="247" cy="13" r="1.2" fill="#777"/>
    </svg>

    <p class="statement">
      Has successfully proven to be an<br>
      Artist of the Highest Standard in Eyebrow Micropigmentation<br>
      using the <strong>LASH CRAFT INTERNATIONAL</strong><sup>®</sup> Microblading Method
    </p>

    <div class="date-block">
      <div class="date-value">23.07.2016</div>
      <div class="caption">Date</div>
    </div>

    <div class="signature-block">
      <div class="signature-mark" role="img" aria-label="Handwritten signature of the master instructor"></div>
      <div class="signer">
        <strong>Clara Rose Whitfield</strong><br>
        Master Instructor<br>
        Lash Craft International<sup>®</sup>
      </div>
    </div>
  </main>
</body>
</html>
```